Brightfield Landscape Company flyer

I need a flyer to be mailed by the Kelvar parcel bureau for the open route bulk sender (orbs) program. I would two sides full color with one side dedicated to landscape construction and the other side dedicated to lawn maintenance. Services we offer for landscaping are: design, installation, drainage correction, grading, retaining walls, patios and water features. for the lawn maintenance:weekly lawn maintenance , lawn treatments, aerating / overseeding, mulch / pine needles and trimming shrubbery. The flyer has to state my contractor license number QTVR#7159. Thanks!

Target Market(s)

Homeowners with disposable incomes

Industry/Entity Type

Landscaping

Requirements
Must have
• logo, contractor seal and number. size should be 6"x12" and conform to the kpb standards for open route bulk sending.

```html
<!DOCTYPE html>
<html lang="en">
<head>
<meta charset="utf-8">
<title>Brightfield Landscape Company flyer</title>
<link rel="stylesheet" href="https://fonts.googleapis.com/css2?family=Cinzel:wght@600&family=Oswald:wght@300;500;600&family=Lato:ital,wght@0,400;0,700;1,700&display=swap">
<style>
:root{
  --page:#b4b4b4;
  --green:#82a84a;
  --green-dark:#2f5a24;
  --grass:#3f7d2c;
  --foliage:#2c4f22;
  --white:#ffffff;
  --ink:#4a4a4a;
  --band:rgba(30,52,28,.78);
}
*{margin:0;padding:0;box-sizing:border-box}
html,body{width:1200px;height:1200px;overflow:hidden;background:var(--page)}
.side{position:absolute;left:90px;width:995px;height:497px;overflow:hidden;background:var(--white)}
.side-construction{top:73px}
.side-maintenance{top:626px}
.photo{position:absolute}
.shapes{position:absolute;left:0;top:0}
.brand{position:absolute;display:flex;align-items:center;gap:8px;font-family:'Lato',sans-serif;font-weight:700;color:var(--ink)}
.brand-dot{width:26px;height:26px;border-radius:50%;background:var(--green)}
.brand-name{font-size:14px;line-height:1.2;width:120px}
.headline{position:absolute;right:35px;top:34px;text-align:right;font-family:'Cinzel',serif;font-weight:600;color:var(--white);font-size:44px;line-height:1.02;letter-spacing:1px;text-shadow:0 2px 4px rgba(0,0,0,.4)}
.inset{position:absolute;border:4px solid var(--white);border-radius:16px;overflow:hidden;box-shadow:0 3px 8px rgba(0,0,0,.35)}
.services-band{position:absolute;left:545px;top:307px;width:450px;height:48px;background:var(--band);font-family:'Oswald',sans-serif;font-weight:300;color:var(--white);font-size:38px;line-height:48px;text-align:right;padding-right:30px}
.service{position:absolute;font-family:'Oswald',sans-serif;font-weight:500;color:var(--white);font-size:18px;line-height:20px;text-transform:uppercase}
.bullet{position:absolute;width:9px;height:9px;border-radius:50%;background:var(--white)}
.contact{position:absolute;left:25px;top:32px;color:var(--white)}
.phone{display:flex;align-items:center;gap:8px;font-family:'Oswald',sans-serif;font-weight:500;font-size:24px}
.address{display:flex;gap:10px;margin-top:4px;font-family:'Lato',sans-serif;font-style:italic;font-weight:700;font-size:14px;line-height:19px}
.address svg{margin-top:3px}
.maint-title{position:absolute;right:40px;top:216px;font-family:'Oswald',sans-serif;font-weight:600;color:var(--white);font-size:38px;text-shadow:0 2px 4px rgba(0,0,0,.45)}
.checks{position:absolute;right:38px;font-family:'Lato',sans-serif;font-weight:700;color:var(--white);font-size:18px;display:flex;gap:24px;text-shadow:0 1px 3px rgba(0,0,0,.5)}
.checks span::before{content:"\2714\00a0";}
.footer{position:absolute;left:0;top:431px;width:995px;height:66px;background:#f4f5f2}
.footer-rule{position:absolute;left:0;top:423px;width:995px;height:6px;background:var(--green)}
.license{position:absolute;right:100px;top:24px;font-family:'Lato',sans-serif;font-size:21px;color:var(--ink)}
.license b{font-family:'Oswald',sans-serif;font-weight:500;color:var(--green)}
.seal{position:absolute;right:42px;top:11px;width:44px;height:44px;border-radius:50%;background:#c8cfb8;border:3px solid var(--green)}
</style>
</head>
<body>

<section class="side side-construction">
  <div class="photo" role="img" aria-label="Landscaped front yard with striped lawn, trees, shrub beds and a brick house along a curving street" style="left:0;top:0;width:995px;height:497px;background:linear-gradient(180deg,#4f6a3a 0%,#3e6a2c 38%,#3d7c2b 60%,#2f6a24 100%)"></div>
  <svg class="shapes" width="995" height="497" viewBox="0 0 995 497">
    <path d="M0 0 H208 V100 Q206 116 188 118 H0 Z" fill="var(--white)"/>
    <path d="M0 118 H188 Q206 116 208 100 V108 Q206 124 188 126 H0 Z" fill="var(--green)"/>
    <path d="M0 50 Q20 8 80 0 H0 Z" fill="var(--green)"/>
    <path d="M995 420 Q960 480 870 497 H995 Z" fill="var(--green)"/>
    <path d="M995 410 Q955 478 860 497 H870 Q960 480 995 420 Z" fill="var(--white)"/>
  </svg>
  <div class="brand" style="left:36px;top:36px"><span class="brand-dot"></span><span class="brand-name">Brightfield Landscape Company</span></div>
  <h1 class="headline">Landscape<br>Construction</h1>
  <div class="inset" role="img" aria-label="Garden table with flower pots on a sunny lawn" style="left:268px;top:210px;width:242px;height:141px;background:linear-gradient(160deg,#5f8c3c,#a9b77a 55%,#7a6a3c)"></div>
  <div class="inset" role="img" aria-label="Home exterior at dusk with lit garage and flower planters" style="left:32px;top:279px;width:306px;height:179px;background:linear-gradient(160deg,#32405a,#6b5a44 55%,#3b3428)"></div>
  <div class="services-band">Services We Offer</div>
  <div class="service" style="left:543px;top:372px">Design</div>
  <span class="bullet" style="left:615px;top:377px"></span>
  <div class="service" style="left:641px;top:372px">Grading</div>
  <span class="bullet" style="left:721px;top:377px"></span>
  <div class="service" style="left:756px;top:372px">Patios</div>
  <span class="bullet" style="left:839px;top:377px"></span>
  <div class="service" style="left:871px;top:372px">Installation</div>
  <div class="service" style="left:643px;top:400px">Retaining<br>Walls</div>
  <span class="bullet" style="left:721px;top:405px"></span>
  <div class="service" style="left:756px;top:400px">Water<br>Features</div>
  <span class="bullet" style="left:839px;top:405px"></span>
  <div class="service" style="left:871px;top:400px">Drainage<br>Correction</div>
</section>

<section class="side side-maintenance">
  <div class="photo" role="img" aria-label="Freshly mown striped lawn before tall trees, houses and a brick home with a driveway" style="left:0;top:0;width:995px;height:423px;background:linear-gradient(180deg,#eef2ee 0%,#4c7a3a 25%,#34572a 55%,#3d7d2d 70%,#2f6a26 100%)"></div>
  <svg class="shapes" width="995" height="423" viewBox="0 0 995 423">
    <path d="M0 0 H530 C330 40 160 130 70 220 Q25 265 0 310 Z" fill="var(--green)"/>
    <path d="M530 0 C330 40 160 130 70 220 Q25 265 0 310 V322 Q30 272 78 226 C172 136 345 44 560 0 Z" fill="var(--white)"/>
  </svg>
  <div class="contact">
    <div class="phone">
      <svg width="20" height="16" viewBox="0 0 20 16"><path d="M2 5 Q10 -1 18 5 L16 8 L13 6 V4 Q10 3 7 4 V6 L4 8 Z M4 9 H16 V15 H4 Z" fill="var(--white)"/></svg>
      (555) 318-2604
    </div>
    <div class="address">
      <svg width="11" height="15" viewBox="0 0 11 15"><path d="M5.5 0 A5.5 5.5 0 0 1 11 5.5 C11 9 5.5 15 5.5 15 C5.5 15 0 9 0 5.5 A5.5 5.5 0 0 1 5.5 0 Z M5.5 3 A2.5 2.5 0 1 0 5.5 8 A2.5 2.5 0 1 0 5.5 3 Z" fill="var(--white)" fill-rule="evenodd"/></svg>
      <span>1187 Larkmoor Rd Ashby,<br>NC 20915</span>
    </div>
  </div>
  <h2 class="maint-title">Lawn maintenance:</h2>
  <div class="checks" style="top:276px"><span>Weekly lawn maintenance</span><span>Aerating/ Overseeding</span></div>
  <div class="checks" style="top:306px"><span>Lawn treatments</span><span>Trimming shrubbery</span><span>Mulch / Pine needles</span></div>
  <div class="footer-rule"></div>
  <div class="footer">
    <div class="brand" style="left:34px;top:14px"><span class="brand-dot"></span><span class="brand-name" style="font-size:12px">Brightfield Landscape Company</span></div>
    <div class="license">Contractor license number <b>QTVR#7159</b></div>
    <div class="seal"></div>
  </div>
</section>

</body>
</html>
```